Byteway Tech Services Flyer

I have a retail Computer Store that I want to promote in the local area.
The target market is seniors aged between 40-80 year olds. I need to create a flyer for the business to do a flyer drop to homes and business advertising the business & services we offer. I would also like to drop this on our socials for online target ads.
Store Name: Byteway Tech systems Address: 17 Larkspur Road, KELVERTON Victoria 3198 Phone Number: (03) 9521 6408 Target Audience: older generation between 40 - 90 year olds Services offered: Retail Sales & Service, Complete Workshop Facilities, Cloud services, Deskly 240 Experts, Network & Wireless Products, Managed Services, PC & Laptop Sales, Custom Built Computers Vendors: Veltrix, QORNL, Parvanix Partner, Olex, Brimo, KT & Rune Reseller Please keep it to A1 size and double sided with options to go A3 o A4 later.

Target Market(s)

Residential home users

Industry/Entity Type

www.bytewaytech.com.au

Font styles to use
Sans Serif

Colors
0054AA
0677BA
7BADD7
CADEEF
E8F1F8

Requirements
Must have
• Simple target is the elderly population

```html
<!DOCTYPE html>
<html lang="en">
<head>
<meta charset="utf-8">
<title>Byteway Tech Services Flyer</title>
<link href="https://fonts.googleapis.com/css2?family=Montserrat:wght@400;500;600;700;800&display=swap" rel="stylesheet">
<style>
:root{
  --navy:#1c4587;
  --navy-deep:#183c78;
  --blue:#0a6cb5;
  --blue-mid:#0677BA;
  --sky:#7BADD7;
  --pale:#CADEEF;
  --mist:#E8F1F8;
  --ink:#333a44;
  --white:#ffffff;
  --backdrop:#9a9a9a;
}
*{box-sizing:border-box;margin:0;padding:0}
html,body{width:1200px;height:841px;overflow:hidden}
body{background:var(--backdrop);font-family:"Montserrat",sans-serif;position:relative;color:var(--ink)}
.page{position:absolute;top:7px;width:585px;height:827px;background:var(--white);overflow:hidden}
.page--front{left:9px}
.page--back{left:604px}

.hero-photo{position:absolute;left:0;top:0;width:585px;height:356px;
  background:radial-gradient(ellipse at 75% 60%,#0d2a44 0,#16466e 25%,transparent 55%),
  linear-gradient(120deg,#b9d3e4 0%,#6fa7cc 35%,#2e6f9e 60%,#d9e6ee 100%)}
.hero-curve{position:absolute;left:0;top:0}
.brand{position:absolute;display:flex;align-items:center;gap:8px}
.brand__mark{width:30px;height:30px;border-radius:5px;background:var(--navy)}
.brand__name{font-weight:700;font-size:21px;letter-spacing:2px;color:var(--navy);white-space:nowrap}
.page--front .brand{left:11px;top:17px}

.intro-box{position:absolute;left:17px;top:194px;width:313px;height:129px;background:var(--navy);opacity:.95;padding:19px 14px 0 17px}
.intro-box h1{color:var(--white);font-size:15px;font-weight:800;line-height:24px;letter-spacing:0;white-space:nowrap}
.intro-box p{color:var(--white);font-size:8.4px;line-height:12px;margin-top:10px;padding-left:2px;white-space:nowrap}

.section-title{position:absolute;left:0;width:100%;text-align:center;color:var(--blue);font-weight:800;font-size:19px;letter-spacing:.3px}
.section-rule{position:absolute;left:50%;width:34px;height:2px;margin-left:-17px;background:var(--blue)}

.offer{position:absolute;width:256px;height:78px;background:var(--white);border-left:5px solid var(--navy);
  box-shadow:0 1px 4px rgba(0,0,0,.18);display:flex;align-items:center}
.offer__icon{flex:none;width:49px;height:49px;border-radius:50%;background:var(--navy);margin-left:6px;display:flex;align-items:center;justify-content:center}
.offer__body{margin-left:11px;padding-right:8px}
.offer h3{color:var(--blue);font-size:10.6px;font-weight:700;line-height:15px}
.offer p{font-size:8.8px;line-height:13px;margin-top:3px;color:var(--ink)}

.footer{position:absolute;left:0;bottom:0;width:585px;height:48px;background:var(--navy)}
.footer__lead{position:absolute;left:13px;top:11px;color:var(--white);font-weight:700;font-size:10px;line-height:14px}
.footer__icon{position:absolute;top:11px;width:26px;height:26px;border-radius:50%;background:var(--white);display:flex;align-items:center;justify-content:center}
.footer__text{position:absolute;color:var(--white);font-size:9px;line-height:12px;white-space:nowrap}

.back-photo{position:absolute;left:0;top:0;width:585px;height:300px;
  background:linear-gradient(180deg,#35528a 0%,#4a6aa3 45%,#5d7db6 100%)}
.back-title{position:absolute;left:0;top:92px;width:100%;text-align:center;color:var(--white);font-weight:800;font-size:24px;letter-spacing:.3px}
.page--back .brand{left:137px;top:266px}

.logo-tile{position:absolute;width:112px;height:55px;background:var(--white);box-shadow:0 1px 4px rgba(0,0,0,.2);
  display:flex;align-items:center;justify-content:center;gap:6px;font-weight:700;font-size:15px;white-space:nowrap}
.logo-tile__sq{width:12px;height:12px;background:#6b6f75}

.why{position:absolute;left:13px;top:549px;width:266px;height:198px;background:var(--white);border-radius:26px;box-shadow:0 1px 6px rgba(0,0,0,.18)}
.why__pill{position:absolute;left:66px;top:529px;width:159px;height:38px;border-radius:19px;background:var(--navy);color:var(--white);
  font-weight:700;font-size:15px;display:flex;align-items:center;justify-content:center}
.checklist{list-style:none}
.checklist li{display:flex;gap:8px;align-items:flex-start;white-space:nowrap}
.checklist svg{flex:none;margin-top:2px}
.why .checklist{position:absolute;left:18px;top:35px;font-size:14px;line-height:17px;color:var(--navy)}
.why .checklist li{margin-bottom:4px}

.help{position:absolute;left:294px;top:529px;width:272px;height:227px;background:var(--navy);border-radius:28px;padding:26px 8px 0 18px;color:var(--white)}
.help h2{font-size:16px;font-weight:700;line-height:20px}
.help .checklist{margin-top:18px;font-size:12.5px;line-height:14px}
.help .checklist li{margin-bottom:3px}
.help .checklist svg{margin-top:1px}
</style>
</head>
<body>

<section class="page page--front">
  <div class="hero-photo" role="img" aria-label="Bright computer store interior with laptops displayed on a white counter"></div>
  <svg class="hero-curve" width="585" height="130" viewBox="0 0 585 130">
    <path d="M0 0 H378 C340 55 250 85 120 92 C50 96 15 110 0 128 Z" fill="#ffffff"/>
  </svg>
  <div class="brand"><span class="brand__mark"></span><span class="brand__name">BYTEWAY TECH SYSTEMS</span></div>

  <div class="intro-box">
    <h1>FOR OUR LOCAL COMMUNITY —<br>SUPPORTING AGES 40 TO 90</h1>
    <p>Large, friendly, trusted computer retail and service centre<br>helping you stay connected, productive, and protected.</p>
  </div>

  <h2 class="section-title" style="top:383px">WHAT WE OFFER</h2>
  <div class="section-rule" style="top:421px"></div>

  <div class="offer" style="left:23px;top:436px">
    <div class="offer__icon"><svg width="26" height="26" viewBox="0 0 26 26" fill="none" stroke="#fff" stroke-width="1.6"><rect x="3" y="4" width="9" height="8"/><circle cx="19" cy="7" r="3"/><path d="M3 18 q6 -4 10 0 l7 -3 M14 9 h3"/></svg></div>
    <div class="offer__body"><h3>Retail Sales &amp; Service</h3><p>Computers, laptops, accessories, and<br>everything you need.</p></div>
  </div>
  <div class="offer" style="left:303px;top:436px">
    <div class="offer__icon"><svg width="26" height="26" viewBox="0 0 26 26" fill="none" stroke="#fff" stroke-width="1.6"><circle cx="13" cy="7" r="4"/><circle cx="6" cy="17" r="2"/><circle cx="13" cy="17" r="2"/><circle cx="20" cy="17" r="2"/><path d="M3 23 h6 M10 23 h6 M17 23 h6"/></svg></div>
    <div class="offer__body"><h3>Complete Workshop Facilities</h3><p>Diagnostics · Repairs · Upgrades ·<br>Tune-ups · Data Recovery</p></div>
  </div>

  <div class="offer" style="left:23px;top:520px">
    <div class="offer__icon"><svg width="26" height="26" viewBox="0 0 26 26" fill="none" stroke="#fff" stroke-width="1.6"><path d="M6 15 a5 5 0 0 1 2 -9 a6 6 0 0 1 11 2 a4 4 0 0 1 1 7"/><ellipse cx="13" cy="14" rx="4" ry="1.6"/><path d="M9 14 v6 a4 1.6 0 0 0 8 0 v-6"/></svg></div>
    <div class="offer__body"><h3>Cloud Services &amp;<br>Deskly 240 Experts</h3><p>Email setups · Cloud storage · Parvanix<br>240 support</p></div>
  </div>
  <div class="offer" style="left:303px;top:520px">
    <div class="offer__icon"><svg width="26" height="26" viewBox="0 0 26 26" fill="none" stroke="#fff" stroke-width="1.6"><rect x="4" y="14" width="18" height="7" rx="1"/><path d="M8 8 a7 7 0 0 1 10 0 M10 11 a4 4 0 0 1 6 0"/><path d="M8 17.5 h2 M13 17.5 h5"/></svg></div>
    <div class="offer__body"><h3>Network &amp; Wireless Setups</h3><p>Home &amp; business Wi-Fi solutions ·<br>Network troubleshooting</p></div>
  </div>

  <div class="offer" style="left:26px;top:605px">
    <div class="offer__icon"><svg width="26" height="26" viewBox="0 0 26 26" fill="none" stroke="#fff" stroke-width="1.6"><rect x="3" y="5" width="20" height="13" rx="1"/><path d="M10 22 h6 M13 18 v4"/><circle cx="9" cy="12" r="3"/><path d="M14 10 h6 M14 13 h5"/></svg></div>
    <div class="offer__body"><h3>Managed IT Services for Home<br>&amp; Business</h3><p>Computers, laptops, accessories, and<br>everything you need.</p></div>
  </div>
  <div class="offer" style="left:303px;top:605px">
    <div class="offer__icon"><svg width="26" height="26" viewBox="0 0 26 26" fill="none" stroke="#fff" stroke-width="1.6"><rect x="3" y="5" width="20" height="13" rx="1"/><path d="M10 22 h6 M13 18 v4"/><circle cx="10" cy="11" r="2.5"/><circle cx="16" cy="11" r="2.5"/></svg></div>
    <div class="offer__body"><h3>PC &amp; Laptop Sales</h3><p>New, refurbished, and performance<br>options.</p></div>
  </div>

  <div class="offer" style="left:24px;top:693px">
    <div class="offer__icon"><svg width="26" height="26" viewBox="0 0 26 26" fill="none" stroke="#fff" stroke-width="1.6"><rect x="3" y="4" width="20" height="18" rx="1.5"/><path d="M3 8 h20 M6 12 l1.5 1.5 l2.5 -2.5 M12 12.5 h4 M6 17 l1.5 1.5 l2.5 -2.5 M12 17.5 h4"/><circle cx="19.5" cy="15" r="2"/></svg></div>
    <div class="offer__body"><h3>Custom-Built Computers</h3><p>Tailored systems for home, business,<br>and gaming.</p></div>
  </div>
  <div class="offer" style="left:303px;top:693px">
    <div class="offer__icon"><svg width="26" height="26" viewBox="0 0 26 26" fill="none" stroke="#fff" stroke-width="1.6"><rect x="3" y="4" width="20" height="18" rx="1.5"/><path d="M3 8 h20 M6 12 l1.5 1.5 l2.5 -2.5 M12 12.5 h4 M6 17 l1.5 1.5 l2.5 -2.5 M12 17.5 h4"/><circle cx="19.5" cy="15" r="2"/></svg></div>
    <div class="offer__body"><h3>Custom Built Computers<br>Vendors</h3><p>Veltrix, QORNL, Parvanix Partner, Olex,<br>Brimo, KT &amp; Rune</p></div>
  </div>

  <footer class="footer">
    <div class="footer__lead">Contact Us For<br>More Information</div>
    <div class="footer__icon" style="left:130px"><svg width="14" height="14" viewBox="0 0 14 14" fill="none" stroke="#1c4587" stroke-width="1.3"><path d="M7 13 C3 8 2.5 6.5 2.5 5 a4.5 4.5 0 0 1 9 0 c0 1.5 -.5 3 -4.5 8z"/><circle cx="7" cy="5" r="1.6"/></svg></div>
    <div class="footer__text" style="left:165px;top:12px">17 Larkspur Road,<br>KELVERTON Victoria 3198</div>
    <div class="footer__icon" style="left:284px"><svg width="14" height="14" viewBox="0 0 14 14" fill="none" stroke="#1c4587" stroke-width="1.3"><path d="M3 1.5 l2 0 l1 3 l-1.5 1 a7 7 0 0 0 4 4 l1 -1.5 l3 1 v2 a1.5 1.5 0 0 1 -1.5 1.5 A10 10 0 0 1 1.5 3 A1.5 1.5 0 0 1 3 1.5z"/></svg></div>
    <div class="footer__text" style="left:321px;top:18px">(03) 9521 6408</div>
    <div class="footer__icon" style="left:405px"><svg width="15" height="15" viewBox="0 0 14 14" fill="none" stroke="#1c4587" stroke-width="1.1"><circle cx="7" cy="7" r="5.8"/><ellipse cx="7" cy="7" rx="2.6" ry="5.8"/><path d="M1.2 7 h11.6 M2 4 h10 M2 10 h10"/></svg></div>
    <div class="footer__text" style="left:441px;top:17px">www.bytewaytech.com.au</div>
  </footer>
</section>

<section class="page page--back">
  <div class="back-photo" role="img" aria-label="Computer store showroom with rows of laptops on display tables, tinted blue"></div>
  <h2 class="back-title">SPECIAL SERVICES FOR SENIORS</h2>
  <svg style="position:absolute;left:0;top:225px" width="585" height="80" viewBox="0 0 585 80">
    <path d="M0 60 C120 20 220 8 292 8 C364 8 470 20 585 60 V80 H0 Z" fill="#ffffff"/>
  </svg>
  <div class="brand"><span class="brand__mark"></span><span class="brand__name">BYTEWAY TECH SYSTEMS</span></div>

  <h2 class="section-title" style="top:324px">BRANDS YOU CAN TRUST</h2>
  <div class="section-rule" style="top:362px"></div>

  <div class="logo-tile" style="left:31px;top:382px;color:#5f6368;font-size:12.5px"><span class="logo-tile__sq"></span>Parvanix Partner</div>
  <div class="logo-tile" style="left:167px;top:382px;color:#1c4587;font-size:17px">Veltrix</div>
  <div class="logo-tile" style="left:304px;top:382px;color:#222;font-size:17px">QORNL</div>
  <div class="logo-tile" style="left:440px;top:382px;color:#1fb36b;font-size:17px">Olex</div>
  <div class="logo-tile" style="left:101px;top:446px;color:#1c5fae;font-size:20px">Brimo</div>
  <div class="logo-tile" style="left:237px;top:446px;color:#0a6cb5;font-size:18px">KT</div>
  <div class="logo-tile" style="left:374px;top:446px;color:#0a6cb5;font-size:17px">Rune</div>

  <div class="why">
    <ul class="checklist">
      <li><svg width="15" height="15" viewBox="0 0 15 15" fill="none" stroke="#1c4587" stroke-width="1.6"><circle cx="7.5" cy="7.5" r="6.3"/><path d="M4.5 7.5 l2.2 2.2 l5 -6"/></svg><span>Locally owned &amp; operated</span></li>
      <li><svg width="15" height="15" viewBox="0 0 15 15" fill="none" stroke="#1c4587" stroke-width="1.6"><circle cx="7.5" cy="7.5" r="6.3"/><path d="M4.5 7.5 l2.2 2.2 l5 -6"/></svg><span>Friendly, patient,<br>senior-friendly service</span></li>
      <li><svg width="15" height="15" viewBox="0 0 15 15" fill="none" stroke="#1c4587" stroke-width="1.6"><circle cx="7.5" cy="7.5" r="6.3"/><path d="M4.5 7.5 l2.2 2.2 l5 -6"/></svg><span>Over 30 years of experience</span></li>
      <li><svg width="15" height="15" viewBox="0 0 15 15" fill="none" stroke="#1c4587" stroke-width="1.6"><circle cx="7.5" cy="7.5" r="6.3"/><path d="M4.5 7.5 l2.2 2.2 l5 -6"/></svg><span>Fast turnaround times</span></li>
      <li><svg width="15" height="15" viewBox="0 0 15 15" fill="none" stroke="#1c4587" stroke-width="1.6"><circle cx="7.5" cy="7.5" r="6.3"/><path d="M4.5 7.5 l2.2 2.2 l5 -6"/></svg><span>Honest advice &amp; expert<br>recommendations</span></li>
    </ul>
  </div>
  <div class="why__pill">Why Choose Us</div>

  <div class="help">
    <h2>Helping You Stay Confident<br>with Technology</h2>
    <ul class="checklist">
      <li><svg width="14" height="14" viewBox="0 0 15 15" fill="none" stroke="#fff" stroke-width="1.6"><circle cx="7.5" cy="7.5" r="6.3"/><path d="M4.5 7.5 l2.2 2.2 l5 -6"/></svg><span>Computer lessons (in-store or<br>remote)</span></li>
      <li><svg width="14" height="14" viewBox="0 0 15 15" fill="none" stroke="#fff" stroke-width="1.6"><circle cx="7.5" cy="7.5" r="6.3"/><path d="M4.5 7.5 l2.2 2.2 l5 -6"/></svg><span>Device setup (phones, tablets,<br>laptops)</span></li>
      <li><svg width="14" height="14" viewBox="0 0 15 15" fill="none" stroke="#fff" stroke-width="1.6"><circle cx="7.5" cy="7.5" r="6.3"/><path d="M4.5 7.5 l2.2 2.2 l5 -6"/></svg><span>Email &amp; online account support</span></li>
      <li><svg width="14" height="14" viewBox="0 0 15 15" fill="none" stroke="#fff" stroke-width="1.6"><circle cx="7.5" cy="7.5" r="6.3"/><path d="M4.5 7.5 l2.2 2.2 l5 -6"/></svg><span>Printer setup and troubleshooting</span></li>
      <li><svg width="14" height="14" viewBox="0 0 15 15" fill="none" stroke="#fff" stroke-width="1.6"><circle cx="7.5" cy="7.5" r="6.3"/><path d="M4.5 7.5 l2.2 2.2 l5 -6"/></svg><span>Home visits available</span></li>
    </ul>
  </div>

  <footer class="footer">
    <div class="footer__lead">Contact Us For<br>More Information</div>
    <div class="footer__icon" style="left:130px"><svg width="14" height="14" viewBox="0 0 14 14" fill="none" stroke="#1c4587" stroke-width="1.3"><path d="M7 13 C3 8 2.5 6.5 2.5 5 a4.5 4.5 0 0 1 9 0 c0 1.5 -.5 3 -4.5 8z"/><circle cx="7" cy="5" r="1.6"/></svg></div>
    <div class="footer__text" style="left:165px;top:12px">17 Larkspur Road,<br>KELVERTON Victoria 3198</div>
    <div class="footer__icon" style="left:284px"><svg width="14" height="14" viewBox="0 0 14 14" fill="none" stroke="#1c4587" stroke-width="1.3"><path d="M3 1.5 l2 0 l1 3 l-1.5 1 a7 7 0 0 0 4 4 l1 -1.5 l3 1 v2 a1.5 1.5 0 0 1 -1.5 1.5 A10 10 0 0 1 1.5 3 A1.5 1.5 0 0 1 3 1.5z"/></svg></div>
    <div class="footer__text" style="left:321px;top:18px">(03) 9521 6408</div>
    <div class="footer__icon" style="left:405px"><svg width="15" height="15" viewBox="0 0 14 14" fill="none" stroke="#1c4587" stroke-width="1.1"><circle cx="7" cy="7" r="5.8"/><ellipse cx="7" cy="7" rx="2.6" ry="5.8"/><path d="M1.2 7 h11.6 M2 4 h10 M2 10 h10"/></svg></div>
    <div class="footer__text" style="left:441px;top:17px">www.bytewaytech.com.au</div>
  </footer>
</section>

</body>
</html>
```